Hoods and pressure washing

We pressure wash house, driveways, buisnesses, gas stations, restraunt hoods and equipments, fences, construction sites and anything that can be pressure washed

Will like my flyer to have written: licenesed, bonded, and insured up to 2 million.(but professionally written)

Target Market(s)

Restraunts, corporations, houses and apartment complexes

Industry/Entity Type

Construction

Colors
33a6d7
33b8a4
ffffff
3176b5

Requirements
Must have
• Before and after pics of dirty and clean pics
Nice to have
• I would like it to be a one paper flyer could be front or back. Company name is aquaBrite. I like a corner written down with all the work we do. Ex: hoods, sidewalks, sidings, houses etc...
• Contact info: Dennis Cawley, phone# 629-415-3307
• Lou Marten, phone # (didnt get one yet)
• Adress: 2417 E. Brantwood rd, portland, Tn, 37162

```html
<!DOCTYPE html>
<html lang="en">
<head>
<meta charset="utf-8">
<title>aquaBrite Pressure Washing Flyer</title>
<link href="https://fonts.googleapis.com/css2?family=Montserrat:wght@300;400;500;600;700;800;900&display=swap" rel="stylesheet">
<style>
  :root {
    --red: #c31d37;
    --navy: #14204a;
    --blue: #1ba3da;
    --dark: #18181a;
    --white: #ffffff;
    --paper: #f2f2f2;
    --ink: #1c1c1c;
  }
  * { box-sizing: border-box; margin: 0; padding: 0; }
  html, body { width: 978px; height: 1200px; overflow: hidden; background: var(--white); }
  body { font-family: 'Montserrat', sans-serif; }
  .flyer { position: relative; width: 978px; height: 1200px; background: var(--paper); overflow: hidden; }

  .intro-panel {
    position: absolute; left: 0; top: 0; width: 420px; height: 690px;
    background: linear-gradient(180deg, #2a2a2b 0%, #1d1d1f 45%, #151516 100%);
    color: var(--white);
  }
  .brand { position: absolute; left: 40px; top: 90px; display: flex; align-items: center; gap: 14px; }
  .brand-dot { width: 44px; height: 44px; border-radius: 50%; background: var(--blue); }
  .brand-name { font-size: 44px; font-weight: 800; color: var(--white); letter-spacing: 0.5px; }

  .welcome { position: absolute; left: 38px; top: 232px; font-size: 25px; font-weight: 400; }
  .headline { position: absolute; left: 36px; top: 262px; font-size: 45px; font-weight: 800; letter-spacing: -0.5px; }
  .headline .accent { color: var(--red); }
  .headline-rule { position: absolute; left: 40px; top: 322px; width: 52px; height: 3px; background: var(--blue); }

  .services-lead { position: absolute; left: 42px; top: 350px; font-size: 15px; font-weight: 600; color: var(--red); }
  .services { position: absolute; left: 46px; top: 373px; list-style: none; }
  .services li { position: relative; padding-left: 20px; font-size: 22px; font-weight: 700; line-height: 30px; }
  .services li::before { content: ""; position: absolute; left: 0; top: 12px; width: 6px; height: 6px; background: var(--red); }
  .services-tail { position: absolute; left: 42px; top: 612px; width: 330px; font-size: 15.5px; font-weight: 600; color: var(--blue); line-height: 21px; }
  .credentials { position: absolute; left: 42px; top: 658px; width: 360px; font-size: 13px; font-weight: 600; color: var(--white); letter-spacing: 0.2px; }

  .photo { position: absolute; }
  .photo-hero { left: 428px; top: 0; width: 550px; height: 690px;
    background: linear-gradient(160deg, #8a8f78 0%, #4d6a3a 28%, #a86a6a 50%, #b67a7a 75%, #c08c8a 100%); }
  .photo-before-after { left: 0; top: 697px; width: 420px; height: 188px;
    background: linear-gradient(90deg, #b9b8b4 0%, #a8a7a3 40%, #5f5f5d 55%, #6d6c68 100%); }
  .photo-deck { left: 426px; top: 697px; width: 282px; height: 188px;
    background: linear-gradient(170deg, #7a6a3e 0%, #8c7a4b 40%, #a89564 70%, #6d5f3f 100%); }
  .photo-concrete { left: 714px; top: 697px; width: 264px; height: 188px;
    background: linear-gradient(135deg, #8c7862 0%, #a79682 50%, #c8bcad 100%); }

  .info-band { position: absolute; left: 0; top: 885px; width: 978px; height: 200px; background: var(--paper); }
  .tagline { position: absolute; left: 38px; top: 20px; font-size: 30px; font-weight: 400; color: var(--ink); line-height: 32px; }
  .tagline-red { position: absolute; left: 38px; top: 88px; font-size: 42px; font-weight: 800; color: var(--red); }
  .tagline-navy { position: absolute; left: 36px; top: 128px; font-size: 56px; font-weight: 900; color: var(--navy); letter-spacing: -0.5px; }
  .divider { position: absolute; left: 397px; top: 20px; height: 155px; border-left: 1px dashed var(--red); }

  .about-title { position: absolute; left: 428px; top: 15px; font-size: 25px; font-weight: 400; color: var(--ink); }
  .about-title strong { color: var(--red); font-weight: 700; }
  .about-rule { position: absolute; left: 430px; top: 52px; width: 52px; height: 3px; background: var(--red); }
  .about-text { position: absolute; left: 430px; top: 66px; width: 485px; font-size: 14px; line-height: 19px; color: var(--ink); text-align: justify; }

  .contact-band { position: absolute; left: 0; top: 1085px; width: 978px; height: 115px; }
  .band-shape { position: absolute; left: 0; top: 0; }
  .people { position: absolute; left: 40px; top: 10px; color: var(--white); }
  .person-name { font-size: 19px; font-weight: 800; letter-spacing: 0.2px; line-height: 23px; }
  .person-phone { display: flex; align-items: center; gap: 6px; font-size: 16px; font-weight: 500; line-height: 20px; margin-bottom: 6px; }
  .icon { flex: none; display: block; }
  .get-in-touch { position: absolute; left: 300px; top: 5px; font-size: 21px; font-weight: 700; color: var(--white); }
  .contact-lines { position: absolute; left: 384px; top: 46px; color: var(--white); font-size: 16px; font-weight: 500; }
  .contact-line { display: flex; align-items: center; gap: 10px; margin-bottom: 8px; line-height: 20px; }
  .contact-line .gap { width: 22px; }
</style>
</head>
<body>
<div class="flyer">

  <section class="intro-panel">
    <div class="brand">
      <span class="brand-dot"></span>
      <span class="brand-name">aquaBrite</span>
    </div>
    <p class="welcome">Welcome To</p>
    <h1 class="headline"><span class="accent">AQUA</span>BRITE</h1>
    <span class="headline-rule"></span>
    <p class="services-lead">We pressure wash</p>
    <ul class="services">
      <li>House</li>
      <li>Driveways</li>
      <li>Buisnesses</li>
      <li>Gas Stations</li>
      <li>Restraunt Hoods and<br>Equipments</li>
      <li>Fences</li>
      <li>Construction Sites</li>
    </ul>
    <p class="services-tail">and anything that can be pressure washed</p>
    <p class="credentials">Fully licensed, bonded &amp; insured up to $2 million</p>
  </section>

  <div class="photo photo-hero" role="img" aria-label="Worker in blue overalls pressure washing red paving stones"></div>
  <div class="photo photo-before-after" role="img" aria-label="Before and after of concrete steps half cleaned"></div>
  <div class="photo photo-deck" role="img" aria-label="Wooden deck being pressure washed"></div>
  <div class="photo photo-concrete" role="img" aria-label="Pressure washer nozzle spraying concrete ground"></div>

  <section class="info-band">
    <p class="tagline">Make it Shine and<br>Sparkle with</p>
    <p class="tagline-red">PRESSURE</p>
    <p class="tagline-navy">WASHING</p>
    <span class="divider"></span>
    <h2 class="about-title">Who <strong>We Are</strong></h2>
    <span class="about-rule"></span>
    <p class="about-text">Lorem Ipsum is simply dummy text of the printing and typesetting industry. Lorem Ipsum has been the industry's standard dummy text ever since the 1500s, when an unknown printer took a galley of type and scrambled it to make a type specimen book. It has survived not only five centuries, but also the leap into electronic typesetting, remaining essentially unchanged.</p>
  </section>

  <footer class="contact-band">
    <svg class="band-shape" width="978" height="115" viewBox="0 0 978 115">
      <polygon points="330,30 978,30 978,115 400,115" fill="#14204a"/>
      <polygon points="0,0 300,0 378,115 0,115" fill="#c31d37"/>
      <polygon points="300,0 318,0 396,115 378,115" fill="#ffffff"/>
      <polygon points="268,0 490,0 500,32 282,32" fill="#1ba3da"/>
    </svg>
    <div class="people">
      <p class="person-name">DENNIS CAWLEY</p>
      <p class="person-phone">
        <svg class="icon" width="14" height="14" viewBox="0 0 14 14"><circle cx="7" cy="7" r="7" fill="#fff"/><path d="M4.3 3.6c.4-.3.9-.2 1.1.2l.6 1.1c.2.4.1.8-.2 1l-.4.3c.4.9 1.1 1.6 2 2l.3-.4c.2-.3.6-.4 1-.2l1.1.6c.4.2.5.7.2 1.1-.5.8-1.4 1-2.3.6C6 9.3 4.7 8 4.1 6.4c-.3-.9-.3-2.2.2-2.8z" fill="#c31d37"/></svg>
        629-415-3307
      </p>
      <p class="person-name">LOU MARTEN</p>
      <p class="person-phone">
        <svg class="icon" width="14" height="14" viewBox="0 0 14 14"><circle cx="7" cy="7" r="7" fill="#fff"/><path d="M4.3 3.6c.4-.3.9-.2 1.1.2l.6 1.1c.2.4.1.8-.2 1l-.4.3c.4.9 1.1 1.6 2 2l.3-.4c.2-.3.6-.4 1-.2l1.1.6c.4.2.5.7.2 1.1-.5.8-1.4 1-2.3.6C6 9.3 4.7 8 4.1 6.4c-.3-.9-.3-2.2.2-2.8z" fill="#c31d37"/></svg>
        629-415-3307
      </p>
    </div>
    <p class="get-in-touch">Get in Touch :</p>
    <div class="contact-lines">
      <p class="contact-line">
        <svg class="icon" width="16" height="18" viewBox="0 0 16 18"><path d="M8 0C4 0 1 3 1 6.8 1 11.5 8 18 8 18s7-6.5 7-11.2C15 3 12 0 8 0z" fill="#c31d37"/><circle cx="8" cy="6.8" r="2.6" fill="#14204a"/></svg>
        2417 E. Brantwood Rd, portland, Tn, 37162
      </p>
      <p class="contact-line">
        <svg class="icon" width="18" height="18" viewBox="0 0 18 18"><circle cx="9" cy="9" r="9" fill="#c31d37"/><rect x="4.5" y="6" width="9" height="6.5" fill="#14204a"/><path d="M4.5 6L9 9.5 13.5 6" stroke="#c31d37" stroke-width="1" fill="none"/></svg>
        hello@aquabritewash.com
        <span class="gap"></span>
        <svg class="icon" width="18" height="18" viewBox="0 0 18 18"><circle cx="9" cy="9" r="9" fill="#c31d37"/><rect x="4.5" y="5.5" width="9" height="7" rx="1" fill="#14204a"/></svg>
        www.aquabritewash.com
      </p>
    </div>
  </footer>

</div>
</body>
</html>
```